IT Services company requires a services website design with integrated blog

We at Brambleway Code Haulage primarily provide application migration consultancy (e.g. moving applications from Paneview QR to Paneview 5) and application virtualization (e.g. Dunmore Box-K) consultancy.This process is commonly known as 'packaging' but doesnt involve cardboard boxes ;) (however, I am happy to use that visual analogy if you want to use any box graphics) We also provide application compatibility testing, software auditing and application portfolio management.

We are looking for a complete redesign of our current horrible diy attempt at a website at www.brambleway-example.com. We have had created a rebranded logo (attached files and fonts) and a rebranded business card (also attached) We would like the website to match the same/similar colors and styling as these.

I want to redisgn the website so that the main focus of this website is to show our subject matter expertise with a blog and should take up most of the websites real estate and focus on the home screen. Then if the customer wants, they can use our services to help them in their own application migration/deployment projects by browsing our details in links/buttons somewhere

In any of the designs, please do not include my Velharo or Dunmore partnerships.  Thank you

Target Market(s)

Application packagers / engineers looking for technical articles

Application migration project managers

Industry/Entity Type

Real Estate

Requirements
Must have
• This site is primarily a blog site. The blog should have buttons to share each article on social media site. It should be easy for me to create or edit new blog articles (have technical skills but not creative ones). Each article should also allow for comments (do not require approval but should allow for admin removal) but do not add like/vote buttons because i do not expect large enough traffic and could be determental.

There should be a contact page to host contact information and an email box that goes to enquiries@brambleway-example.com

The other pages should include About us and Services (placeholder text to be used as current site text needs overhauling but original text can be used in the design just remember when placing that the text may shorten or increase etc.)

All text has to be easily editable (no over use of text in images where possible)
Nice to have
• An email notification of new comments to articles sent to webadmin@brambleway-example.com

Newsletter subscription
Should not have
• Do not include vote/like buttons or website counters. Initial traffic is not going to be large enough to warrant these features and may reflect badly on the site.

No logon features. Site content and commenting should be open access

No opinion polls

No why choose us section from current website

Do not include partner information in new site (Velharo and Dunmore)

DO NOT JUST REPLICATE EXISTING WEBSITE FEATURES, PLEASE REFER TO THIS BRIEF. THIS SITE NEEDS TO PRIMARILY BE A BLOG

```html
<!DOCTYPE html>
<html lang="en">
<head>
<meta charset="utf-8">
<title>Brambleway Code Haulage</title>
<link href="https://fonts.googleapis.com/css2?family=Open+Sans:wght@300;400;600;700&display=swap" rel="stylesheet">
<style>
  :root {
    --blue: #3a62b5;
    --blue-dark: #2b4c97;
    --ink: #222;
    --text: #444;
    --muted: #777;
    --paper: #f1f1f1;
    --band: #2b2b2b;
    --line: #d6d6d6;
    --white: #fff;
  }
  * { box-sizing: border-box; margin: 0; padding: 0; }
  html, body { width: 904px; height: 1200px; overflow: hidden; }
  body { font-family: "Open Sans", Arial, sans-serif; background: var(--paper); color: var(--text); position: relative; }

  .site-header { position: absolute; top: 0; left: 0; width: 904px; height: 72px; background: linear-gradient(#f6f6f6, #dcdcdc); border-bottom: 2px solid #b9b9b9; }
  .brand { position: absolute; left: 70px; top: 22px; display: flex; align-items: center; gap: 8px; }
  .brand-mark { width: 22px; height: 22px; border-radius: 50%; background: var(--blue); }
  .brand-name { font-size: 17px; font-weight: 400; color: #555; }
  .main-nav { position: absolute; top: 6px; right: 70px; display: flex; }
  .nav-item { width: 95px; text-align: center; font-size: 11px; color: var(--ink); text-transform: uppercase; }
  .nav-item svg { display: block; margin: 0 auto 4px; }
  .nav-item.active { color: var(--blue); }

  .hero { position: absolute; top: 72px; left: 0; width: 904px; height: 400px; background: radial-gradient(ellipse at 60% 45%, #6b6f76 0%, #3a3d42 45%, #151618 100%); }
  .hero-copy { position: absolute; left: 70px; top: 130px; width: 230px; color: var(--white); font-size: 18.5px; font-weight: 600; line-height: 22px; }
  .btn-pill { display: inline-block; border-radius: 20px; background: linear-gradient(#5a80cf, var(--blue-dark)); color: var(--white); font-weight: 600; border: 2px solid #8ea8de; text-align: center; }
  .hero-cta { position: absolute; left: 70px; top: 212px; width: 120px; height: 34px; line-height: 30px; font-size: 17px; }

  .slider-dots { position: absolute; top: 494px; left: 366px; display: flex; gap: 7px; }
  .slider-dots span { width: 38px; height: 3px; background: #d8d8d8; }
  .slider-dots span.on { background: var(--blue); }

  .section-title { color: var(--blue); font-size: 23.5px; font-weight: 600; line-height: 32px; }
  .btn-dark { display: inline-block; background: #2a2a2a; color: #eee; font-size: 10px; border-radius: 12px; height: 22px; line-height: 20px; border: 1px solid #000; padding: 0 8px; text-align: center; }

  .blog { position: absolute; left: 70px; top: 522px; width: 440px; }
  .article-list { margin-top: 10px; }
  .article { display: flex; gap: 14px; height: 66px; }
  .article-thumb { width: 58px; height: 58px; flex: none; }
  .article h3 { font-size: 14px; font-weight: 600; color: var(--ink); line-height: 18px; }
  .meta { font-size: 10px; color: var(--muted); margin-top: 4px; line-height: 13px; }
  .meta a { color: var(--blue); text-decoration: none; }
  .blog .btn-dark { position: absolute; top: 246px; left: 0; width: 70px; }

  .divider { position: absolute; left: 530px; top: 530px; width: 1px; height: 250px; background: linear-gradient(transparent, var(--line), transparent); }

  .welcome { position: absolute; left: 550px; top: 522px; width: 300px; }
  .welcome h2 { color: var(--blue); font-size: 16px; font-weight: 600; line-height: 32px; }
  .welcome p { font-size: 11px; line-height: 16.5px; margin-top: 2px; }
  .welcome p + p { margin-top: 10px; }
  .welcome .btn-dark { position: absolute; top: 246px; left: 0; }

  .services { position: absolute; top: 812px; left: 0; width: 904px; height: 338px; background: var(--band); color: var(--white); }
  .services h2 { position: absolute; top: 17px; width: 100%; text-align: center; font-size: 22px; font-weight: 700; }
  .service { position: absolute; top: 85px; width: 170px; text-align: center; }
  .service svg { display: block; margin: 0 auto; height: 50px; }
  .service h3 { font-size: 15px; font-weight: 600; margin-top: 15px; }
  .service p { width: 152px; margin: 8px auto 0; font-size: 11px; font-weight: 400; line-height: 16px; color: #e2e2e2; }
  .services .btn-pill { position: absolute; top: 279px; left: 376px; width: 118px; height: 34px; line-height: 30px; font-size: 17px; }

  .site-footer { position: absolute; top: 1150px; left: 0; width: 904px; height: 50px; border-top: 1px solid #ccc; font-size: 10px; color: #888; }
  .footer-links { position: absolute; left: 70px; top: 18px; display: flex; gap: 20px; }
  .copyright { position: absolute; right: 70px; top: 18px; }
</style>
</head>
<body>
  <header class="site-header">
    <div class="brand"><span class="brand-mark"></span><span class="brand-name">Brambleway Code Haulage</span></div>
    <nav class="main-nav">
      <div class="nav-item active">
        <svg width="36" height="36" viewBox="0 0 36 36"><circle cx="18" cy="18" r="17" fill="#3a62b5" stroke="#8ea8de" stroke-width="2"/><path d="M9 18 L18 10 L27 18 M12 17 V26 H16 V21 H20 V26 H24 V17" fill="#fff"/></svg>Home
      </div>
      <div class="nav-item">
        <svg width="36" height="36" viewBox="0 0 36 36"><g fill="#333"><circle cx="12" cy="15" r="3"/><circle cx="18" cy="13" r="3.5"/><circle cx="24" cy="15" r="3"/><path d="M7 24 q5-7 10 0z M12 24 q6-9 12 0z M19 24 q5-7 10 0z"/></g></svg>About Us
      </div>
      <div class="nav-item">
        <svg width="36" height="36" viewBox="0 0 36 36"><g fill="#333"><circle cx="18" cy="18" r="8"/><g stroke="#333" stroke-width="4"><path d="M18 7v22M7 18h22M10 10l16 16M26 10L10 26"/></g></g><circle cx="18" cy="18" r="3.5" fill="#ddd"/></svg>Services
      </div>
    </nav>
  </header>

  <section class="hero" role="img" aria-label="Photo of a hand touching a cloud diagram of platform, application and infrastructure services above two tablets">
    <p class="hero-copy">We offer most efficient standards in application virtualization</p>
    <span class="btn-pill hero-cta">Contact Us</span>
  </section>

  <div class="slider-dots"><span class="on"></span><span></span><span></span><span></span></div>

  <section class="blog">
    <h1 class="section-title">Latest Articles</h1>
    <div class="article-list">
      <article class="article">
        <div class="article-thumb" role="img" aria-label="Thumbnail photo of a person with glowing technology icons" style="background:linear-gradient(135deg,#1c2a3a,#c8742a 60%,#2a3d55)"></div>
        <div><h3>De nombreuses suites logicielles</h3><p class="meta">Posted by Wren 1 hour ago</p><p class="meta">Tagged with: <a>Distractions</a>, <a>Ressemblent</a>, <a>logicielles</a></p></div>
      </article>
      <article class="article">
        <div class="article-thumb" role="img" aria-label="Thumbnail photo of a person before a board of sketched ideas" style="background:linear-gradient(135deg,#efe6c8,#c9b98a 55%,#8a8f95)"></div>
        <div><h3>De nombreuses suites logicielles</h3><p class="meta">Posted by Wren 1 hour ago</p><p class="meta">Tagged with: <a>Distractions</a>, <a>Ressemblent</a>, <a>logicielles</a></p></div>
      </article>
      <article class="article">
        <div class="article-thumb" role="img" aria-label="Thumbnail photo of a network map over server racks" style="background:linear-gradient(160deg,#5d9bd8,#2a5f99 55%,#1a2a40)"></div>
        <div><h3>De nombreuses suites logicielles</h3><p class="meta">Posted by Wren 1 hour ago</p><p class="meta">Tagged with: <a>Distractions</a>, <a>Ressemblent</a>, <a>logicielles</a></p></div>
      </article>
    </div>
    <span class="btn-dark">View All</span>
  </section>
  <div class="divider"></div>

  <aside class="welcome">
    <h2>Welcome to Brambleway Code Haulage</h2>
    <p>Le Lorem Ipsum est simplement du faux texte employé dans la composition et la mise en page avant impression. Le Lorem Ipsum est le faux texte standard de l'imprimerie depuis les années 1500.</p>
    <p>quand un peintre anonyme assembla ensemble des morceaux de texte pour réaliser un livre spécimen de polices de texte. Il n'a pas fait que survivre cinq siècles, mais s'est aussi adapté à la bureatique informatique, sans que son contenu n'en soit modifié. Il a été popularisé dans les années 1960.</p>
    <span class="btn-dark">Read More</span>
  </aside>

  <section class="services">
    <h2>Our Services</h2>
    <div class="service" style="left:81px">
      <svg viewBox="0 0 50 50" width="50"><g fill="none" stroke="#fff" stroke-width="2"><rect x="6" y="3" width="26" height="36" rx="3"/><circle cx="19" cy="25" r="7"/><circle cx="19" cy="25" r="2"/><circle cx="19" cy="10" r="2"/><path d="M38 37l9 9M47 37l-9 9" stroke-width="3"/></g></svg>
      <h3>Initialisation</h3>
      <p>Contrairement à une opinion répandue, le Lorem Ipsum n'est pas simplement du texte aléa-toire Il trouve ses.</p>
    </div>
    <div class="service" style="left:271px">
      <svg viewBox="0 0 50 50" width="50"><g fill="none" stroke="#fff" stroke-width="2"><rect x="3" y="8" width="40" height="30"/><rect x="8" y="13" width="40" height="30" fill="#2b2b2b"/></g><path d="M12 39 L22 27 L30 34 L36 29 L44 39Z" fill="#fff"/><circle cx="20" cy="20" r="3" fill="#fff"/></svg>
      <h3>Portfolio Management</h3>
      <p>Contrairement à une opinion répandue, le Lorem Ipsum n'est pas simplement du texte aléa-toire Il trouve ses.</p>
    </div>
    <div class="service" style="left:462px">
      <svg viewBox="0 0 50 50" width="50"><g fill="none" stroke="#fff" stroke-width="2"><rect x="7" y="6" width="36" height="38" rx="2"/><path d="M7 18h36M25 6v12"/></g></svg>
      <h3>Packaging</h3>
      <p>Contrairement à une opinion répandue, le Lorem Ipsum n'est pas simplement du texte aléa-toire Il trouve ses.</p>
    </div>
    <div class="service" style="left:654px">
      <svg viewBox="0 0 50 50" width="50"><path d="M14 36 a10 10 0 0 1 0-20 a12 12 0 0 1 23-2 a10 10 0 0 1 0 22z" fill="#fff"/><path d="M25 46V26M18 32l7-8 7 8" fill="none" stroke="#2b2b2b" stroke-width="4"/><path d="M25 48V26M18 32l7-8 7 8" fill="none" stroke="#fff" stroke-width="2.5"/></svg>
      <h3>Virtualization</h3>
      <p>Contrairement à une opinion répandue, le Lorem Ipsum n'est pas simplement du texte aléa-toire Il trouve ses.</p>
    </div>
    <span class="btn-pill">View All</span>
  </section>

  <footer class="site-footer">
    <nav class="footer-links"><span>Home</span><span>About Us</span><span>Services</span></nav>
    <p class="copyright">Copyright © 2013. All rights reserved.</p>
  </footer>
</body>
</html>
```